Business Card Design using new logo

As much as we'd like to think that treating everyone equally is the best strategy for fairness, the reality is that the differences in the lives of women and men have to be taken into account to ensure that organizations, programs, services, and yes, even public policy treat women and men in ways that achieve gender equity.

That's where ParityLoom - balance insight metrics comes in. Using the data-driven tools of gender analysis, our organization can help anyone determine if gender equity is being achieved - in businesses and organizations, in the planning and implementation of programs and services, and in the development and enforcement of public policy.
Updates

Apologies for the delay - have not had time to finalize the decision.  Should be early this week - probably Tuesday.

Industry/Entity Type

Business

Requirements
Must have
• New Logo for ParityLoom
• Logo plus words "Balance Insight Metrics"

```html
<!DOCTYPE html>
<html lang="en">
<head>
<meta charset="utf-8">
<title>ParityLoom – Business Card</title>
<link href="https://fonts.googleapis.com/css2?family=Ubuntu:wght@300;400;500&display=swap" rel="stylesheet">
<style>
  :root {
    --stage: #d9d9d9;
    --card-light: #ffffff;
    --card-dark: #231f21;
    --ink: #1d1d1d;
    --muted: #a6a6a6;
    --accent: #f08a1c;
    --accent-deep: #d9771a;
    --on-dark: #ffffff;
  }
  * { box-sizing: border-box; margin: 0; padding: 0; }
  html, body { width: 1200px; height: 900px; overflow: hidden; }
  body {
    background: var(--stage);
    font-family: "Ubuntu", sans-serif;
    display: flex;
    flex-direction: column;
    align-items: center;
    justify-content: center;
    gap: 48px;
  }
  .card {
    position: relative;
    width: 640px;
    height: 366px;
    overflow: hidden;
    box-shadow: 0 10px 30px rgba(0,0,0,.25);
  }

  /* back */
  .card--back {
    background: var(--card-dark);
    display: flex;
    align-items: center;
    justify-content: center;
    gap: 18px;
  }
  .card--back .brand-dot {
    width: 46px; height: 46px; border-radius: 50%;
    background: var(--accent);
  }
  .card--back .brand-name {
    color: var(--on-dark);
    font-size: 44px;
    font-weight: 400;
  }

  /* front */
  .card--front { background: var(--card-light); color: var(--ink); }
  .tagline {
    position: absolute; left: 380px; top: 34px;
    font-size: 13px; font-weight: 300; letter-spacing: .06em;
    text-transform: uppercase; color: var(--muted); line-height: 1.2;
  }
  .brand {
    position: absolute; left: 44px; top: 98px;
    display: flex; align-items: center; gap: 14px;
  }
  .brand .brand-dot {
    width: 38px; height: 38px; border-radius: 50%;
    background: var(--accent);
  }
  .brand .brand-name { font-size: 36px; font-weight: 400; color: var(--ink); }
  .person { position: absolute; left: 96px; top: 162px; }
  .person-name { font-size: 21px; color: var(--accent); font-weight: 400; }
  .person-role { font-size: 14px; margin-top: 1px; }
  .contacts { position: absolute; left: 96px; top: 224px; font-size: 15px; }
  .contacts li { list-style: none; display: flex; align-items: center; gap: 8px; line-height: 20px; }
  .contacts .gap { height: 12px; }
  .contacts svg { width: 12px; height: 12px; flex: none; fill: var(--accent); }
  .bars { position: absolute; right: 0; bottom: 58px; }
  .bars rect { fill: var(--accent); }
</style>
</head>
<body>

  <section class="card card--back" aria-label="Card back">
    <span class="brand-dot"></span>
    <span class="brand-name">ParityLoom</span>
  </section>

  <section class="card card--front" aria-label="Card front">
    <p class="tagline">Balance<br>Insight Metrics</p>

    <div class="brand">
      <span class="brand-dot"></span>
      <span class="brand-name">ParityLoom</span>
    </div>

    <div class="person">
      <p class="person-name">Marcus Hallworth</p>
      <p class="person-role">managing director</p>
    </div>

    <ul class="contacts">
      <li><svg viewBox="0 0 12 12"><path d="M2.5 1l2 2.5-1 1.2a6 6 0 0 0 3.8 3.8l1.2-1 2.5 2-1.3 1.5C5.5 11 1 6.5 1 2.3z"/></svg>4410 203 118</li>
      <li><svg viewBox="0 0 12 12"><path d="M3 0h6a1 1 0 0 1 1 1v10a1 1 0 0 1-1 1H3a1 1 0 0 1-1-1V1a1 1 0 0 1 1-1zm.5 1.5v7.5h5V1.5zM6 9.8a.7.7 0 1 0 0 1.4.7.7 0 0 0 0-1.4z"/></svg>7720 415 906</li>
      <li class="gap"></li>
      <li><svg viewBox="0 0 12 12"><path d="M0 2h12v8H0zm1 1l5 3.5L11 3z"/></svg>mhallworth@parityloom.com</li>
      <li><svg viewBox="0 0 12 12"><rect width="12" height="12" rx="1.5"/></svg>@Parity_Loom</li>
      <li><svg viewBox="0 0 12 12"><path d="M6 0a6 6 0 1 0 0 12A6 6 0 0 0 6 0zm0 1.2c.8.8 1.3 2.3 1.4 4.2H4.6C4.7 3.5 5.2 2 6 1.2zM1.2 6.6h2.3c.1 1.6.5 3 1.1 4A4.8 4.8 0 0 1 1.2 6.6zm0-1.2a4.8 4.8 0 0 1 3.4-4c-.6 1-1 2.4-1.1 4zM6 10.8c-.8-.8-1.3-2.3-1.4-4.2h2.8c-.1 1.9-.6 3.4-1.4 4.2zm1.4-.2c.6-1 1-2.4 1.1-4h2.3a4.8 4.8 0 0 1-3.4 4zm1.1-5.2c-.1-1.6-.5-3-1.1-4a4.8 4.8 0 0 1 3.4 4z"/></svg>www.parityloom.com</li>
    </ul>

    <svg class="bars" width="250" height="230" viewBox="0 0 250 230" role="img" aria-label="Rising bar chart">
      <rect x="0" y="128" width="72" height="102"/>
      <rect x="90" y="66" width="72" height="164"/>
      <rect x="180" y="0" width="70" height="230"/>
    </svg>
  </section>

</body>
</html>
```